Software company WebSite Design (enterprise level SW, Mobile apps, HW prototypes)

We need design for our new webpages. We got new logo and new business cards and we need webdesign which will be match with those two.
We are dealing with corporate level software development - enterprise level portals, development of optimalization SW, route planning optimalizations. For a few months we are developing mobile applications for companies.
IMPORTANT is to express the cutting edge technological company.

Target Market(s)

IT company customers

Industry/Entity Type

Business

Number of Pages Required

2 page

Requirements
Must have
• Project needs to have landing page and product detail page. Design needs to be created including full font and example images as there would be a real webpage. Design should be clean, modern and expressing hi-tech level of the company.
• Example of well designer web pages - www.quolvent.com, www.brandovi.com - We like the font formatting and font designs (colors, placing, etc - its professional).
• Attached image contains screenshot from old web landing page. It contains basic sections of our business (Simulation Tools, Enterprise Intranet Systems, Hi-tech web presentations, Supporting Enterprise services - Optimalization and logistics monitoring)

```html
<!DOCTYPE html>
<html lang="en">
<head>
<meta charset="utf-8">
<title>KORVEX Solutions</title>
<link href="https://fonts.googleapis.com/css2?family=Open+Sans:wght@400;600;700&display=swap" rel="stylesheet">
<style>
:root{
  --blue:#1a8fd8;
  --ink:#3a3f47;
  --muted:#6b7079;
  --light:#f3f5f9;
  --navy:#1f3a52;
  --dark:#232b36;
  --footer:#1f252e;
  --footer-deep:#181d24;
  --white:#ffffff;
  --logo-grey:#a9adb3;
}
*{margin:0;padding:0;box-sizing:border-box}
html,body{width:762px;height:1200px;overflow:hidden}
body{font-family:"Open Sans",Arial,sans-serif;color:var(--ink);background:var(--white);position:relative}
.abs{position:absolute}
.btn{position:absolute;background:var(--blue);color:var(--white);font-size:7.5px;font-weight:600;display:flex;align-items:center;justify-content:center;gap:5px}
.btn svg{width:9px;height:7px}

/* header */
.site-header{position:absolute;left:0;top:0;width:762px;height:45px;background:var(--white)}
.brand{position:absolute;left:57px;top:9px;display:flex;align-items:center;gap:6px}
.brand-mark{width:22px;height:22px;background:var(--blue)}
.brand-name{font-size:19px;font-weight:700;color:var(--ink);letter-spacing:.5px}
.main-nav{position:absolute;left:266px;top:19px;display:flex;gap:17px;font-size:7px;color:var(--muted)}
.main-nav .active{color:var(--blue);position:relative}
.main-nav .active::before{content:"";position:absolute;left:-8px;right:-8px;top:-19px;height:2px;background:var(--blue)}
.sign-in{left:635px;top:11px;width:70px;height:23px}

/* hero */
.hero{position:absolute;left:0;top:45px;width:762px;height:291px;background:linear-gradient(120deg,#1b2c3d 0%,#24415b 45%,#1d3a52 100%)}
.hero h1{position:absolute;left:0;width:762px;top:116px;text-align:center;color:var(--white);font-size:20px;font-weight:700;letter-spacing:.3px}
.hero p{position:absolute;left:0;width:762px;top:143px;text-align:center;color:var(--white);font-size:7.5px}
.hero .btn{left:338px;top:163px;width:86px;height:22px}
.slide-arrow{position:absolute;width:8px;height:9px}
.dots{position:absolute;left:372px;top:267px;display:flex;gap:4px;align-items:flex-end}
.dots span{width:2px;height:6px;background:var(--white)}
.dots span.on{height:12px;background:var(--blue)}

/* services */
.section-title{position:absolute;left:0;width:762px;text-align:center;font-size:14px;color:var(--ink)}
.service{position:absolute;width:160px;text-align:center}
.service .ring{width:78px;height:78px;margin:0 auto;border:1.5px solid var(--ink);border-radius:50%;display:flex;align-items:center;justify-content:center}
.service .ring.on{border-color:var(--blue)}
.service .ring svg{width:34px;height:34px}
.service h3{font-size:7.5px;font-weight:600;margin-top:13px;letter-spacing:.2px}

/* presentation */
.showcase{position:absolute;left:0;top:508px;width:762px;height:250px;background:var(--light)}
.photo{position:absolute}
.showcase h2{position:absolute;left:387px;top:36px;font-size:14px;font-weight:400}
.showcase p{position:absolute;left:387px;top:62px;width:318px;font-size:7.5px;line-height:14.1px;color:var(--muted)}
.showcase .btn{left:387px;top:185px;width:80px;height:22px}

/* support */
.support{position:absolute;left:0;top:758px;width:762px;height:191px;background:linear-gradient(180deg,#2a323e,#1f2630)}
.support .section-title{color:var(--white);top:24px}
.gauge{position:absolute;width:170px;text-align:center;color:var(--white)}
.gauge svg{width:84px;height:84px;display:block;margin:0 auto}
.gauge h4{font-size:7.5px;font-weight:400;line-height:11px;margin-top:11px}

/* customers */
.customer{position:absolute;top:1004px;display:flex;align-items:center;gap:4px;font-size:15px;font-weight:700;color:var(--logo-grey)}
.customer i{width:14px;height:14px;background:var(--logo-grey);display:block}
.customer.featured{color:var(--ink)}
.customer.featured i{background:var(--blue)}

/* footer */
.site-footer{position:absolute;left:0;top:1051px;width:762px;height:149px;background:var(--footer);color:var(--white)}
.site-footer h5{font-size:11px;font-weight:700;margin-bottom:7px}
.col{position:absolute;top:21px;font-size:7px;line-height:11.3px}
.col ul{list-style:none}
.newsletter{margin-top:8px;width:135px;height:18px;border-bottom:1px solid #4a525e;display:flex;justify-content:space-between;align-items:center;color:#c6cad1;padding-left:6px}
.social{display:flex;gap:12px;margin-top:8px}
.social span{width:7px;height:7px;border-radius:50%;background:#aeb3bb}
.contact-row{display:flex;gap:8px;margin-bottom:5px}
.contact-row svg{width:6px;height:7px;flex:none;margin-top:2px}
.footer-bottom{position:absolute;left:0;top:120px;width:762px;height:29px;background:var(--footer-deep);font-size:7px;padding:11px 0 0 58px}
.to-top{position:absolute;left:682px;top:111px;width:23px;height:23px;border-radius:50%;background:var(--white);display:flex;align-items:center;justify-content:center}
</style>
</head>
<body>

<header class="site-header">
  <div class="brand"><span class="brand-mark"></span><span class="brand-name">KORVEX</span></div>
  <nav class="main-nav">
    <span class="active">HOME</span><span>PRODUCTS</span><span>CUSTOMERS</span><span>PRICING</span><span>DEVELOPERS</span><span>SUPPORT</span><span>RESOURCES</span>
  </nav>
  <div class="btn sign-in">Sign in <svg viewBox="0 0 9 7"><path d="M0 3.5h8M5 .5l3 3-3 3" fill="none" stroke="#fff" stroke-width=".9"/></svg></div>
</header>

<section class="hero" role="img" aria-label="Dark blue photo of a businessman working at a laptop">
  <svg class="slide-arrow" style="left:24px;top:142px" viewBox="0 0 8 9"><path d="M7 .5v8L1 4.5z" fill="none" stroke="#fff"/></svg>
  <svg class="slide-arrow" style="left:729px;top:142px" viewBox="0 0 8 9"><path d="M1 .5v8l6-4z" fill="none" stroke="#1a8fd8"/></svg>
  <h1>WELCOME TO KORVEX</h1>
  <p>Nulla consequat massa quis enim donec pede justo fringilla vel aliquet nec.</p>
  <div class="btn">Learn More <svg viewBox="0 0 9 7"><path d="M0 3.5h8M5 .5l3 3-3 3" fill="none" stroke="#fff" stroke-width=".9"/></svg></div>
  <div class="dots"><span class="on"></span><span></span><span></span></div>
</section>

<h2 class="section-title" style="top:356px;font-weight:400">What We Provide</h2>
<div class="service" style="left:57px;top:387px">
  <div class="ring"><svg viewBox="0 0 34 34"><circle cx="17" cy="17" r="14" fill="none" stroke="#3a3f47" stroke-width="1.8"/><path d="M5 13c5 0 6 4 9 4s2 6 0 10M22 5c-2 4 1 6 4 7s5 4 4 7M17 17c4 1 6 3 5 8" fill="none" stroke="#3a3f47" stroke-width="1.8"/></svg></div>
  <h3>ENTERPRISE PORTAL</h3>
</div>
<div class="service" style="left:220px;top:387px">
  <div class="ring on"><svg viewBox="0 0 34 34"><circle cx="21" cy="9" r="3" fill="none" stroke="#1a8fd8" stroke-width="1.3"/><circle cx="11" cy="17" r="3" fill="none" stroke="#1a8fd8" stroke-width="1.3"/><circle cx="21" cy="25" r="3" fill="none" stroke="#1a8fd8" stroke-width="1.3"/><path d="M13.5 15.5l5-4.5M13.5 18.5l5 4.5" stroke="#1a8fd8" stroke-width="1.3"/></svg></div>
  <h3>OPTIMALIZATION SW</h3>
</div>
<div class="service" style="left:383px;top:387px">
  <div class="ring"><svg viewBox="0 0 34 34"><path d="M17 4a4 4 0 0 1 4 4c0 3-4 8-4 8s-4-5-4-8a4 4 0 0 1 4-4z" fill="none" stroke="#3a3f47" stroke-width="1.3"/><circle cx="17" cy="8" r="1.3" fill="#3a3f47"/><path d="M17 18v5M17 23l-8 4M17 23l8 4" stroke="#3a3f47" stroke-width="1.3"/><circle cx="8" cy="27.5" r="1.8" fill="#3a3f47"/><circle cx="26" cy="27.5" r="1.8" fill="#3a3f47"/></svg></div>
  <h3>ROUTE PLANING OPTIMALIZATION</h3>
</div>
<div class="service" style="left:545px;top:387px">
  <div class="ring"><svg viewBox="0 0 34 34"><rect x="8" y="5" width="12" height="22" rx="1.5" fill="none" stroke="#3a3f47" stroke-width="1.3"/><path d="M8 9h12M8 23h12" stroke="#3a3f47" stroke-width="1"/><circle cx="24" cy="21" r="3" fill="none" stroke="#3a3f47" stroke-width="1.3"/><circle cx="24" cy="21" r="5" fill="none" stroke="#3a3f47" stroke-width="1.3" stroke-dasharray="2 1.6"/></svg></div>
  <h3>MOBILE APPLICATIONS</h3>
</div>

<section class="showcase">
  <svg class="slide-arrow" style="left:24px;top:119px" viewBox="0 0 8 9"><path d="M7 .5v8L1 4.5z" fill="none" stroke="#b8bcc3"/></svg>
  <svg class="slide-arrow" style="left:729px;top:119px" viewBox="0 0 8 9"><path d="M1 .5v8l6-4z" fill="none" stroke="#1a8fd8"/></svg>
  <div class="photo" style="left:57px;top:39px;width:100px;height:167px;background:linear-gradient(135deg,#3b3f46,#1d2025)" role="img" aria-label="Photo of an electronics workbench"></div>
  <div class="photo" style="left:225px;top:39px;width:124px;height:167px;background:linear-gradient(135deg,#5c5a57,#cfc9c2)" role="img" aria-label="Photo of hands writing in a notebook beside a coffee cup"></div>
  <div class="photo" style="left:125px;top:23px;width:107px;height:194px;border-radius:6px;background:#15181d;padding:10px 3px 20px" role="img" aria-label="Smartphone showing the company name">
    <div style="width:100%;height:100%;background:#fff;display:flex;align-items:center;justify-content:center;font-size:14px;font-weight:700;color:#3a3f47">KORVEX</div>
  </div>
  <h2>Hi-tech web presentations</h2>
  <p>Integer tincidunt. Cras dapibus. Vivamus elementum semper nisi. Aenean vulputate eleifend tellus. Aenean leo ligula, porttitor eu, consequat vitae, eleifend ac, enim. Aliquam lorem ante, dapibus in, viverra quis, feugiat a, tellus. Phasellus viverra nulla ut metus varius laoreet. Quisque rutrum. Aenean imperdiet. Etiam ultricies nisi vel augue. Curabitur ullamcorper ultricies nisi. Nam eget dui. Etiam rhoncus. Maecenas tempus, tellus eget condimentum rhoncus, sem quam semper libero, sit amet adipiscing sem neque sed ipsum. Nam quam nunc, blandit vel, luctus pulvinar, hendrerit id, lorem.</p>
  <div class="btn">Read More <svg viewBox="0 0 9 7"><path d="M0 3.5h8M5 .5l3 3-3 3" fill="none" stroke="#fff" stroke-width=".9"/></svg></div>
</section>

<section class="support" role="img" aria-label="Dark photo of a keyboard behind the support figures">
  <h2 class="section-title" style="font-weight:400">Our Support</h2>
  <div class="gauge" style="left:80px;top:55px">
    <svg viewBox="0 0 84 84"><circle cx="42" cy="42" r="40" fill="none" stroke="#3e4652" stroke-width="1.6"/><path d="M42 2a40 40 0 0 1 40 42" fill="none" stroke="#1a8fd8" stroke-width="1.8"/><circle cx="82" cy="44" r="4" fill="#fff" stroke="#9aa0a8"/><text x="42" y="46" text-anchor="middle" fill="#fff" font-size="11" font-weight="700" font-family="Open Sans, sans-serif">5Hrs</text></svg>
    <h4>RESPONSE TIME FOR<br>TICKET PRE-SCREENING</h4>
  </div>
  <div class="gauge" style="left:296px;top:55px">
    <svg viewBox="0 0 84 84"><circle cx="42" cy="42" r="40" fill="none" stroke="#3e4652" stroke-width="1.6"/><path d="M42 2a40 40 0 1 1 -40 32" fill="none" stroke="#1a8fd8" stroke-width="1.8"/><circle cx="3" cy="34" r="4" fill="#fff" stroke="#9aa0a8"/><text x="42" y="46" text-anchor="middle" fill="#fff" font-size="11" font-weight="700" font-family="Open Sans, sans-serif">17Hrs</text></svg>
    <h4>RESPONSE TIME FOR<br>ISSUE ESCALATION</h4>
  </div>
  <div class="gauge" style="left:512px;top:55px">
    <svg viewBox="0 0 84 84"><circle cx="42" cy="42" r="40" fill="none" stroke="#1a8fd8" stroke-width="1.8"/><circle cx="42" cy="3" r="4" fill="#fff" stroke="#9aa0a8"/><text x="42" y="46" text-anchor="middle" fill="#fff" font-size="11" font-weight="700" font-family="Open Sans, sans-serif">24Hrs</text></svg>
    <h4>RESPONSE TIME<br>FOR TICKETS</h4>
  </div>
</section>

<h2 class="section-title" style="top:968px;font-weight:400">Our Customers</h2>
<div class="customer" style="left:76px"><i></i>KORVEX</div>
<div class="customer" style="left:206px"><i></i>KORVEX</div>
<div class="customer featured" style="left:335px"><i></i>KORVEX</div>
<div class="customer" style="left:465px"><i></i>KORVEX</div>
<div class="customer" style="left:595px"><i></i>KORVEX</div>

<footer class="site-footer">
  <div class="col" style="left:57px;width:170px">
    <h5>About</h5>
    <p>Aenean vulputate eleifend tellus aenean leo ligula porttitor eu consequat vitae eleifend ac enim aliquam lorem ante dapibus in viverra quis feugiat a tellus phasellus viverra nulla ut metus varius laoreet quisque rutrum eenean imperdiet etiam ultricies nisi vel auguec urabitur.</p>
  </div>
  <div class="col" style="left:280px">
    <h5>Useful Links</h5>
    <ul><li>- Services</li><li>- Our Work</li><li>- Reviews</li><li>- Products</li><li>- Developers</li><li>- Contacts</li></ul>
  </div>
  <div class="col" style="left:398px;width:145px">
    <h5>Follow Us</h5>
    <p>Subscribe to our newsletter to get latest updates and offers.</p>
    <div class="newsletter">Enter email <svg width="8" height="7" viewBox="0 0 8 7"><path d="M0 3l8-3-2 7-2-2.5z" fill="#c6cad1"/></svg></div>
    <div class="social"><span></span><span></span><span></span></div>
  </div>
  <div class="col" style="left:575px;width:140px">
    <h5>Contact information</h5>
    <div class="contact-row"><svg viewBox="0 0 6 7"><path d="M3 7S0 4 0 2.6a3 3 0 0 1 6 0C6 4 3 7 3 7z" fill="#fff"/></svg><span>Some address line here..., area info, City name, Country name.</span></div>
    <div class="contact-row"><svg viewBox="0 0 6 7"><path d="M1 0l1.5 1.8-.8 1a4 4 0 0 0 1.8 1.8l1-.8L6 5.5 5 7C2 6.5 0 4 0 1z" fill="#fff"/></svg><span>123 456 7890</span></div>
    <div class="contact-row"><svg viewBox="0 0 6 7"><rect x="0" y="1.5" width="6" height="4" fill="#fff"/><path d="M0 1.5l3 2 3-2" stroke="#1f252e" stroke-width=".6" fill="none"/></svg><span>info@korvex.com</span></div>
  </div>
  <div class="footer-bottom">© KORVEX, All rights reserved.</div>
  <div class="to-top"><svg width="7" height="5" viewBox="0 0 7 5"><path d="M.5 4L3.5 1l3 3" fill="none" stroke="#3a3f47"/></svg></div>
</footer>

</body>
</html>
```